Business Card Design

Marla Quibbet
Artist of Contemporary/Modern/Representational Art
Contact: 0457219308
Please include my web site (thanks)! http://www.artvault913.com.au/marla-quibbet
And
Email: marlaquibbet@fernpost.example

Target Market(s)

Modern professional People who know what they like in modern contemporary art and have the means to purchase it.

Industry/Entity Type

Business

Contact Information for Business Card

Marla Quibbet
Contact: 0457219308

Font styles to use
Sans Serif

Requirements
Must have
• Simplicity & to the point
Keep the font modern/ contemporary
Nice to have
• A portrait of me and one piece of work on the business card (one on each side).
Should not have
• I'm not into butterflies.
No feminine style swirls
Nor I like swirls that look like tatoos

```html
<!DOCTYPE html>
<html lang="en">
<head>
<meta charset="utf-8">
<title>Marla Quibbet — Business Card</title>
<link rel="stylesheet" href="https://fonts.googleapis.com/css2?family=Titillium+Web:ital,wght@0,300;0,400;1,600;1,700&display=swap">
<style>
  :root {
    --card-core: #3a3a3a;
    --card-mid: #1f1f1f;
    --card-edge: #050505;
    --ink-light: #ffffff;
    --accent-blue: #3ab2e4;
    --icon-ink: #141414;
  }
  html, body {
    margin: 0;
    padding: 0;
    width: 1200px;
    height: 742px;
    overflow: hidden;
    background: var(--card-edge);
  }
  .card {
    position: relative;
    width: 1200px;
    height: 742px;
    overflow: hidden;
    background:
      radial-gradient(ellipse 70% 75% at 48% 42%, var(--card-core) 0%, var(--card-mid) 55%, var(--card-edge) 100%);
    font-family: "Titillium Web", sans-serif;
  }
  .identity {
    position: absolute;
    right: 644px;
    top: 300px;
    text-align: right;
  }
  .identity__name {
    margin: 0;
    color: var(--ink-light);
    font-weight: 400;
    font-size: 90px;
    line-height: 1;
    letter-spacing: 0.5px;
    white-space: nowrap;
  }
  .identity__role {
    margin: 14px 0 0;
    color: var(--accent-blue);
    font-style: italic;
    font-weight: 700;
    font-size: 20px;
    line-height: 27px;
    letter-spacing: 0.6px;
  }
  .contacts {
    position: absolute;
    left: 614px;
    top: 334px;
    margin: 0;
    padding: 0;
    list-style: none;
  }
  .contacts__item {
    display: flex;
    align-items: center;
    height: 28px;
    margin-bottom: 17px;
    color: var(--ink-light);
    font-weight: 400;
    font-size: 22px;
    white-space: nowrap;
  }
  .contacts__icon {
    flex: none;
    width: 28px;
    height: 28px;
    margin-right: 8px;
    background: var(--accent-blue);
    border-radius: 3px;
  }
  .contacts__icon svg {
    display: block;
    width: 28px;
    height: 28px;
  }
</style>
</head>
<body>
  <main class="card">
    <section class="identity">
      <h1 class="identity__name">Marla Quibbet</h1>
      <p class="identity__role">Artist of Contemporary/Modern<br>Representational Art</p>
    </section>

    <ul class="contacts">
      <li class="contacts__item">
        <span class="contacts__icon">
          <svg viewBox="0 0 28 28" aria-hidden="true">
            <path d="M9 6.5c.8-.6 1.8-.4 2.2.4l1.4 2.8c.3.7.1 1.4-.5 1.8l-1.2.8c.8 2 2.4 3.7 4.4 4.6l.9-1.1c.5-.6 1.2-.7 1.9-.4l2.7 1.5c.8.4 1 1.4.4 2.2l-1.1 1.4c-.7.9-2 1.2-3.1.8C12 20 8.1 16 6.9 11.4c-.3-1.1 0-2.3.9-3z" fill="var(--icon-ink)"/>
          </svg>
        </span>
        0457219308
      </li>
      <li class="contacts__item">
        <span class="contacts__icon">
          <svg viewBox="0 0 28 28" aria-hidden="true">
            <circle cx="14" cy="14" r="7.5" fill="none" stroke="var(--icon-ink)" stroke-width="2"/>
            <ellipse cx="14" cy="14" rx="3.2" ry="7.5" fill="none" stroke="var(--icon-ink)" stroke-width="1.6"/>
            <line x1="6.5" y1="14" x2="21.5" y2="14" stroke="var(--icon-ink)" stroke-width="1.6"/>
          </svg>
        </span>
        http://www.artvault913.com.au/marla-quibbet
      </li>
      <li class="contacts__item">
        <span class="contacts__icon">
          <svg viewBox="0 0 28 28" aria-hidden="true">
            <rect x="6.5" y="8.5" width="15" height="11" rx="1" fill="var(--icon-ink)"/>
            <path d="M7.5 9.5l6.5 5 6.5-5" fill="none" stroke="var(--accent-blue)" stroke-width="1.4"/>
          </svg>
        </span>
        marlaquibbet@fernpost.example
      </li>
    </ul>
  </main>
</body>
</html>
```